Bright Harbor Crew, and interior design project management company!

We invite you to participate in our logo and web design contest for "Bright Harbor Crew Management Corp."!

Here's a brief description of our company paraphrased by ChatGPT.

Company Overview:
Bright Harbor Crew Management Corp. is your trusted partner for interior design project management, guided by international standards set forth by the Worksite Planning Guild (WPG) and the Canon of Build Practice Standards (CBPS). With a commitment to excellence, we seamlessly merge modern project management techniques with traditional values, emphasizing quality and attention to detail in every project.

Our Unique Strengths:

Local Fabrication Facility: What sets us apart is our in-house fabrication facility, a millwork shop with an impressive 20 years of experience. This facility empowers us to exercise meticulous control over the production process, ensuring that your project is crafted with precision and care right in our local community.

Experienced Skilled Workers: At Bright Harbor Crew Management Corp., our team comprises highly skilled and experienced craftsmen and artisans. They bring years of expertise to every project, guaranteeing that your interior design visions are brought to life with unmatched skill and finesse.

Serving Commercial and Residential Clients:
Our primary focus is on serving commercial clients, specializing in Tenant Improvement (TI) projects. We understand the unique demands of commercial spaces, and our project management expertise ensures that your commercial interior design projects are executed efficiently and within budget.

In addition to our commercial expertise, we also cater to discerning residential clients who seek that extra level of attention to detail. Our comprehensive services encompass all types of projects, from commercial tenant improvements to residential renovations. Regardless of the project's scale or scope, you can trust that all aspects will be managed seamlessly by our professional team.

Why Choose Us:
We are not just project managers; we are passionate advocates for your project's success. By adhering to WPG and CBPS standards, we deliver project management that is structured, efficient, and dependable. Our commitment to personal and approachable service, combined with our dedication to quality craftsmanship, ensures that your interior design projects are executed flawlessly from start to finish.

With Bright Harbor Crew Management Corp., you can trust that your project will benefit from the perfect blend of modern project management techniques and traditional values, resulting in interiors that are not only aesthetically pleasing but also built to stand the test of time.

Whether you require a commercial TI project or a residential project with meticulous attention to detail, we are the one-stop professional company that can bring your vision to life. Join our logo design contest, and let's together represent our dedication to excellence in project management and craftsmanship for both commercial and residential clients.

interior designers and architects, business owners

construction, project management, interior design, custom millwork and cabinets

1 page

• General consideration for design to float from social media to website.
• Consideration for more sophisticated backend support for customer support and project management update integrations apps such as ClickUp. (Technical portion not part of scope of work.)

```html
<!DOCTYPE html>
<html lang="en">
<head>
<meta charset="utf-8">
<title>Bright Harbor Crew Management Corp.</title>
<link href="https://fonts.googleapis.com/css2?family=Josefin+Sans:wght@300;400;600;700&display=swap" rel="stylesheet">
<style>
:root{
  --ink:#2a2b2f;
  --text:#3c3d42;
  --slate:#4a4d55;
  --gold:#b39467;
  --gold-dark:#8f7550;
  --line:#cfcfcf;
  --paper:#ffffff;
  --foot:#efefef;
}
*{box-sizing:border-box;margin:0;padding:0}
html,body{width:1200px;height:5040px;overflow:hidden}
body{background:var(--paper);font-family:"Josefin Sans",sans-serif;color:var(--text);position:relative}
.abs{position:absolute}
.nav{left:340px;top:0;width:520px;height:40px;border:1px solid var(--line);border-top:none;display:flex;justify-content:space-around;align-items:center;font-size:12px;letter-spacing:.5px;color:var(--ink)}
.nav a{color:inherit;text-decoration:none;padding:8px 12px}
.nav a.active{background:#e6e6e6}
.brand{left:0;width:1200px;text-align:center;color:var(--ink);font-weight:600}
.brand .name{font-size:44px;letter-spacing:1px;line-height:1}
.brand .sub{font-size:18px;letter-spacing:3px;margin-top:6px}
.brand .mark{width:22px;height:22px;border:2px solid var(--ink);margin:0 auto 14px}
.hero{left:0;top:260px;width:1200px;height:580px;background:radial-gradient(ellipse at 50% 55%,#6b4a2c 0%,#3a2616 45%,#1a120c 100%)}
.hero h1{position:absolute;top:228px;width:100%;text-align:center;color:#fff;font-weight:400;font-size:46px;letter-spacing:6px}
.btn{display:inline-block;background:var(--gold);color:#fff;font-size:11px;letter-spacing:1px;padding:7px 12px 5px;text-transform:uppercase}
.btn.dark{background:#5a4a36}
.hero .btn{position:absolute;top:318px;left:548px}
.dots{position:absolute;top:536px;left:0;width:100%;display:flex;justify-content:center;gap:10px}
.dots i{width:8px;height:8px;border-radius:50%;background:#fff;opacity:.55}
.dots i:first-child{opacity:1}
.sec-title{left:0;width:1200px;text-align:center}
.sec-title span{display:inline-block;background:var(--paper);border:1px solid var(--line);padding:14px 26px 10px;font-size:30px;font-weight:600;letter-spacing:1px;color:var(--ink);line-height:1.1}
.ph{position:absolute}
.service{position:absolute;top:992px;width:376px;text-align:center}
.service .ph{position:static;height:408px}
.service h3{margin-top:40px;font-size:26px;font-weight:600;letter-spacing:1px;color:var(--ink)}
.service p{font-size:13px;line-height:1.45;margin:8px auto 14px;width:230px;color:var(--ink)}
.welcome{left:0;top:1592px;width:1200px;height:560px;background:var(--slate)}
.welcome .box{position:absolute;left:132px;top:70px;width:420px;border:1px solid #9b9ea6;padding:16px 18px 10px;color:#fff;font-size:27px;font-weight:600;line-height:1.2;letter-spacing:1px;white-space:nowrap}
.welcome p{position:absolute;left:132px;top:228px;width:380px;color:#e4e4e6;font-size:13px;line-height:1.5}
.welcome .btn{position:absolute;left:132px;top:450px}
.welcome .ph{left:648px;top:28px;width:536px;height:480px}
.intro{left:300px;top:2280px;width:600px;text-align:center;font-size:14px;line-height:1.5;color:var(--ink)}
.card{position:absolute;top:2420px;width:252px;height:460px;border:1px solid var(--line);text-align:center;padding:28px 20px}
.card svg{display:block;margin:0 auto}
.card h4{margin-top:26px;font-size:19px;font-weight:600;line-height:1.3;color:var(--ink)}
.card p{margin-top:14px;font-size:13px;line-height:1.45;color:var(--ink)}
.why-img{left:0;top:2944px;width:560px;height:588px}
.why{left:560px;top:2988px;width:640px;height:500px;background:var(--slate);color:#fff;padding:86px 70px 0 92px}
.why h2{font-size:32px;font-weight:600;letter-spacing:1px}
.why p{margin-top:28px;font-size:13px;line-height:1.5;color:#e4e4e6}
.why p+p{margin-top:16px}
.why .btn{margin-top:20px}
.lead{left:0;width:1200px;top:3756px;text-align:center;font-size:14px;color:var(--ink)}
.grid .ph{width:304px;height:368px}
.more{left:548px;top:4630px}
.footer{left:0;top:4700px;width:1200px;height:340px;background:var(--foot)}
.footer .brand{top:66px}
.footer nav{position:absolute;top:232px;width:100%;display:flex;justify-content:center;gap:40px;font-size:12px;color:var(--ink)}
.footer small{position:absolute;top:282px;width:100%;text-align:center;font-size:12px;color:var(--ink)}
</style>
</head>
<body>

<nav class="nav abs"><a class="active">HOME</a><a>ABOUT US</a><a>SERVICES</a><a>PORTFOLIO</a><a>CONTACT US</a></nav>

<div class="brand abs" style="top:88px">
  <div class="mark"></div>
  <div class="name">BRIGHT HARBOR CREW</div>
  <div class="sub">MANAGEMENT CORP</div>
</div>

<section class="hero abs" role="img" aria-label="Restaurant interior with curved wooden slatted ceiling and dining tables">
  <h1>INTERIOR DESIGN COMPANY</h1>
  <span class="btn">Read more</span>
  <div class="dots"><i></i><i></i><i></i></div>
</section>

<svg class="abs" style="left:588px;top:862px" width="24" height="12" viewBox="0 0 24 12"><path d="M2 2 L12 10 L22 2" fill="none" stroke="var(--gold)" stroke-width="2"/></svg>

<div class="sec-title abs" style="top:888px"><span>OUR SERVICES</span></div>

<div class="service" style="left:16px">
  <div class="ph" role="img" aria-label="Office interior with plants and wooden furniture" style="background:linear-gradient(160deg,#d9d6cf,#8b8577 60%,#5a5a4a)"></div>
  <h3>TENANT IMPROVEMENT</h3>
  <p>Lorem Ipsum is simply dummy text of the printing and typesetting.</p>
  <span class="btn">Read more</span>
</div>
<div class="service" style="left:412px">
  <div class="ph" role="img" aria-label="Bright modern interior with wooden staircase" style="background:linear-gradient(160deg,#f2f2f0,#c9c3b8 55%,#7a6a55)"></div>
  <h3>COMMERCIAL</h3>
  <p>Lorem Ipsum is simply dummy text of the printing and typesetting.</p>
  <span class="btn">Read more</span>
</div>
<div class="service" style="left:808px">
  <div class="ph" role="img" aria-label="Residential living room with sofa and large windows" style="background:linear-gradient(160deg,#e8e6e2,#a9a49b 55%,#4e4c48)"></div>
  <h3>RESIDENTIAL</h3>
  <p>Lorem Ipsum is simply dummy text of the printing and typesetting.</p>
  <span class="btn">Read more</span>
</div>

<section class="welcome abs">
  <div class="box">WELCOME TO<br>BRIGHT HARBOR CREW<br>MANAGEMENT CORP</div>
  <p>Bright Harbor Crew Management Corp. is your trusted partner for interior design project management, guided by international standards set forth by the Worksite Planning Guild (WPG) and the Canon of Build Practice Standards (CBPS). With a commitment to excellence, we seamlessly merge modern project management techniques with traditional values, emphasizing quality and attention to detail in every project.</p>
  <span class="btn">Read more</span>
  <div class="ph" role="img" aria-label="Open-plan living space with mezzanine and tall windows" style="background:linear-gradient(150deg,#eceae6,#b7b1a6 50%,#5b564f)"></div>
</section>

<div class="sec-title abs" style="top:2204px"><span>OUR UNIQUE STRENGTHS</span></div>
<p class="intro abs">In addition to our commercial expertise, we also cater to discerning residential clients who seek that extra level of attention to detail. Our comprehensive services encompass all types of projects, from commercial tenant improvements to residential renovations. Regardless of the project's scale or scope, you can trust that all aspects will be managed seamlessly by our professional team.</p>

<div class="card" style="left:158px">
  <svg width="64" height="64" viewBox="0 0 64 64" fill="none" stroke="var(--gold)" stroke-width="2"><rect x="8" y="8" width="48" height="48"/><path d="M8 24H56M24 8V56M40 24V56"/></svg>
  <h4>LOCAL FABRICATION<br>FACILITY</h4>
  <p>What sets us apart is our in-house fabrication facility, a millwork shop with an impressive 20 years of experience. This facility empowers us to exercise meticulous control over the production process, ensuring that your project is crafted with precision and care right in our local community.</p>
</div>
<div class="card" style="left:474px">
  <svg width="64" height="64" viewBox="0 0 64 64" fill="none" stroke="var(--gold)" stroke-width="2"><path d="M14 30a18 18 0 0 1 36 0H14z"/><path d="M10 30H54M32 12V22"/><path d="M20 56V40H44V56"/></svg>
  <h4>EXPERIENCED<br>SKILLED WORKERS</h4>
  <p>At Bright Harbor Crew Management Corp., our team comprises highly skilled and experienced craftsmen and artisans. They bring years of expertise to every project, guaranteeing that your interior design visions are brought to life with unmatched skill and finesse.</p>
</div>
<div class="card" style="left:790px">
  <svg width="64" height="64" viewBox="0 0 64 64" fill="none" stroke="var(--gold)" stroke-width="2"><path d="M8 56H56"/><rect x="12" y="36" width="10" height="20"/><rect x="27" y="24" width="10" height="32"/><rect x="42" y="12" width="10" height="44"/></svg>
  <h4>SERVING COMMERCIAL<br>AND RESIDENTIAL<br>CLIENTS</h4>
  <p>Our primary focus is on serving commercial clients, specializing in Tenant Improvement (TI) projects. We understand the unique demands of commercial spaces, and our project management expertise ensures that your commercial interior design projects are executed efficiently and within budget.</p>
</div>

<div class="ph why-img" role="img" aria-label="Dark kitchen with pendant lights and long wooden dining table" style="background:linear-gradient(160deg,#cfcfcd,#6d6f72 45%,#2b2c2f)"></div>
<section class="why abs">
  <h2>WHY CHOOSE US</h2>
  <p>We are not just project managers; we are passionate advocates for your project's success. By adhering to WPG and CBPS standards, we deliver project management that is structured, efficient, and dependable. Our commitment to personal and approachable service, combined with our dedication to quality craftsmanship, ensures that your interior design projects are executed flawlessly from start to finish.</p>
  <p>With Bright Harbor Crew Management Corp., you can trust that your project will benefit from the perfect blend of modern project management techniques and traditional values, resulting in interiors that are not only aesthetically pleasing but also built to stand the test of time.</p>
  <span class="btn">Read more</span>
</section>

<div class="sec-title abs" style="top:3664px"><span>GET INSPIRED.</span></div>
<p class="lead abs">From design to lifestyle, everything you need to make life beautiful.</p>

<div class="grid">
  <div class="ph" style="left:132px;top:3812px;background:linear-gradient(160deg,#8a6f58,#4a3a2e)" role="img" aria-label="Dining room with dark wood panelling"></div>
  <div class="ph" style="left:448px;top:3812px;background:linear-gradient(160deg,#b99c7c,#5d4734)" role="img" aria-label="Warm lounge with wooden shelving"></div>
  <div class="ph" style="left:764px;top:3812px;background:linear-gradient(160deg,#f0ece4,#c7b79d)" role="img" aria-label="Light dining area with wooden chairs"></div>
  <div class="ph" style="left:132px;top:4212px;background:linear-gradient(160deg,#f4f3f1,#b8b3ac)" role="img" aria-label="White room with hanging pendant lamps"></div>
  <div class="ph" style="left:448px;top:4212px;background:linear-gradient(160deg,#e6e3de,#9c958b)" role="img" aria-label="Bright living room with pendant light"></div>
  <div class="ph" style="left:764px;top:4212px;background:linear-gradient(160deg,#2e2c2a,#8a7a66)" role="img" aria-label="Dark dining room with round table"></div>
</div>
<span class="btn dark more abs">View all</span>

<footer class="footer abs">
  <div class="brand abs">
    <div class="mark"></div>
    <div class="name">BRIGHT HARBOR CREW</div>
    <div class="sub">MANAGEMENT CORP</div>
  </div>
  <nav><span>HOME</span><span>ABOUT US</span><span>SERVICES</span><span>PORTFOLIO</span><span>CONTACT US</span></nav>
  <small>Copyright © 2023 All Rights Reserved</small>
</footer>

</body>
</html>
```